Product Label Design

We require 2 labels, with the same look and feel, designed for our range of trucking related products for the transport industry. Our logo has been provided.

In terms of the look and feel, we are after:
- a clean and elegant design to represent our premium range of products. By clean we mean not "too busy" or cluttered
- masculine as this relates to trucking,
- must convey that our products are cutting-edge and innovative (our competitors' labels are outdated and dull thus we want to stand-out in the world market)

We want you to create a standardised label template for us, which we can use for several products. We will simply change the product description and product code and reprint.

Each product label will have a:
• Product Description
• Product code
• An image or artwork of a truck as all our products are for the transport industry
• Display product Size in bottom right hand corner
Label 1: 20L (180 mm x 180 mm with 5 mm radius on corners )
Label 2: 750ml (A copy of the 750ml bottle die line has been unloaded as a PDF)

You may use text placeholders for the description.

Files Required:
We need the final design as a psd file, as our business uses Photoshop CS6.

REFERENCE:
Attached is an sample label with the features we want (ie product description, product size, and so on). Please DO NOT use or see this as a reference for your design or style we are after. We do not want your creativity to be restricted by this sample.

Target Market(s)

Products for the trucking industry

Industry/Entity Type

Industry

Colors

Designer to choose colors to be used in the design.

Requirements
Must have
• Logo
• • Image of a truck on the label (preferably the truck should be cutting edge and modern to align it with our product)
• • Some type of background
• • Product description
• • Product code
• • Product size on Bottom Right corner
Should not have
• Unnecessary graphics that will clutter the design

```html
<!DOCTYPE html>
<html lang="en">
<head>
<meta charset="utf-8">
<title>Korva Freight – Product Labels</title>
<link rel="stylesheet" href="https://fonts.googleapis.com/css2?family=Montserrat:wght@800&family=Open+Sans:wght@600;700&display=swap">
<style>
  :root {
    --backdrop: #d3d3d3;
    --label-white: #f4f4f4;
    --label-black: #050505;
    --copper: #c8925c;
    --copper-dark: #7a4f2a;
    --copper-light: #e0b387;
    --ink: #1e1e1e;
    --size-text: #ffffff;
  }
  * { box-sizing: border-box; margin: 0; padding: 0; }
  html, body { width: 1200px; height: 773px; overflow: hidden; }
  body { background: var(--backdrop); position: relative; font-family: "Open Sans", sans-serif; }

  .label {
    position: absolute;
    overflow: hidden;
    background: var(--label-white);
    box-shadow: 0 3px 8px rgba(0,0,0,0.25);
  }
  .label--bottle {
    left: 94px; top: 168px; width: 392px; height: 438px;
    border-radius: 50% 50% 12px 12px / 80px 80px 12px 12px;
  }
  .label--drum {
    left: 597px; top: 130px; width: 518px; height: 513px;
    border-radius: 12px;
  }

  .brand {
    position: absolute; left: 0; right: 0;
    display: flex; align-items: center; justify-content: center; gap: 10px;
  }
  .brand__dot { border-radius: 50%; background: var(--copper); flex: none; }
  .brand__name {
    font-family: "Montserrat", sans-serif; font-weight: 800;
    color: var(--ink); line-height: 0.95; letter-spacing: 1px;
  }
  .label--bottle .brand { top: 40px; }
  .label--bottle .brand__dot { width: 30px; height: 30px; }
  .label--bottle .brand__name { font-size: 30px; }
  .label--drum .brand { top: 22px; }
  .label--drum .brand__dot { width: 38px; height: 38px; }
  .label--drum .brand__name { font-size: 40px; }

  .panel {
    position: absolute; left: 0; right: 0; bottom: 0;
    background: var(--label-black); overflow: hidden;
  }
  .label--bottle .panel { top: 142px; }
  .label--drum .panel { top: 144px; }

  .halo {
    position: absolute; border-radius: 50%;
    border: 1px solid var(--copper-dark);
    outline: 2px dotted var(--copper-dark); outline-offset: 6px;
  }
  .label--bottle .halo { left: 58px; top: -34px; width: 276px; height: 276px; }
  .label--drum .halo { left: 78px; top: -52px; width: 360px; height: 360px; }

  .truck-art {
    position: absolute; border-radius: 6px;
    background: linear-gradient(180deg, var(--copper-light), var(--copper) 45%, var(--copper-dark));
  }
  .label--bottle .truck-art { left: 116px; top: 14px; width: 160px; height: 176px; }
  .label--drum .truck-art { left: 152px; top: 14px; width: 210px; height: 230px; }

  .description-band {
    position: absolute; background: var(--copper);
    border-top: 2px solid var(--label-black);
    box-shadow: 0 -3px 0 var(--copper-dark), 0 3px 0 var(--copper-dark);
    display: flex; align-items: center; justify-content: space-between;
    padding: 0 14px; color: var(--ink);
  }
  .description-band__name { font-weight: 700; text-transform: uppercase; letter-spacing: 0.5px; }
  .description-band__code { font-weight: 600; }
  .label--bottle .description-band { left: 18px; top: 203px; width: 356px; height: 40px; font-size: 14px; }
  .label--drum .description-band { left: 14px; top: 256px; width: 490px; height: 51px; font-size: 18px; padding: 0 18px; }

  .size {
    position: absolute; color: var(--size-text); font-weight: 600;
  }
  .label--bottle .size { right: 20px; bottom: 16px; font-size: 19px; }
  .label--drum .size { right: 22px; bottom: 14px; font-size: 31px; letter-spacing: 1px; }
</style>
</head>
<body>

  <section class="label label--bottle">
    <div class="brand">
      <span class="brand__dot"></span>
      <span class="brand__name">KORVA<br>FREIGHT</span>
    </div>
    <div class="panel">
      <div class="halo"></div>
      <div class="truck-art" role="img" aria-label="Front view illustration of a modern truck in copper tones"></div>
      <div class="description-band">
        <span class="description-band__name">Product Description</span>
        <span class="description-band__code">Code: KF-0000</span>
      </div>
      <p class="size">750ml</p>
    </div>
  </section>

  <section class="label label--drum">
    <div class="brand">
      <span class="brand__dot"></span>
      <span class="brand__name">KORVA<br>FREIGHT</span>
    </div>
    <div class="panel">
      <div class="halo"></div>
      <div class="truck-art" role="img" aria-label="Front view illustration of a modern truck in copper tones"></div>
      <div class="description-band">
        <span class="description-band__name">Product Description</span>
        <span class="description-band__code">Code: KF-0000</span>
      </div>
      <p class="size">20L</p>
    </div>
  </section>

</body>
</html>
```